Zielgruppe
Wir arbeiten in folgenden Bereichen:
- Mediation
- Konfliktmanagement
- Coaching
- Training
- Teamtraining
Über eine professionelle Webseite möchten wir neue Kunden gewinnen. Dazu möchten wir uns und unsere Leistungen vorstellen sowie dem Benutzer die Möglichkeit geben, sich über unsere anstehenden Projekte und Events zu informieren sowie uns zu kontaktieren.
Zielgruppe: Unsere Arbeit richtet sich an alle. Im Fokus stehen dabei Unternehmen. Theoretisch ist aber auch Arbeit mit Privatpersonen denkbar.
Aufgabenstellung
Farben: Dunkelblau, hellblau, weiß - Siehe Farben im PDF-Anhang. Eine weitere Akzentfarbe ist möglich.
Es geht ausschließlich um das Webdesign. Keine technische Umsetzung ist gewünscht.
Schriften: Bitte nur freie Schriften verwenden. Am besten wären Google Fonts.
Freie Stockfotos dürfen verwendet werden.
Das Design muss auf Desktop (optimiert auf ca. 1400px) und Mobile funktionieren (Responsive).
Nice to have wären optimierte App- und Favicons die auch vom Logo abweichen dürfen.
Die Seite wird mehrsprachig sein.
Für die Icons nur freie Icons verwenden.
Uns gefallen diese Seiten sehr gut. Es darf sich gern daran orientiert werden:
https://ufer-sieben.de/de/
https://bolmerhof.com
Wir wünschen uns ein komponentenbasiertes Design. Es soll uns möglich sein, die Komponenten frei zu kombinieren und neue Seiten zu kreieren. Als Vorgaben möchten wir gern die drei Seiten haben, die unten folgen.
Lieferung bitte in Figma. Das Resultat muss später in unseren Account übertragen werden können.

```html
<!DOCTYPE html>
<html lang="de">
<head>
<meta charset="utf-8">
<title>Weg zum Dialog – Mediation, Coaching, Teamtraining</title>
<link href="https://fonts.googleapis.com/css2?family=Lexend:wght@300;400;500;600&display=swap" rel="stylesheet">
<style>
:root{
  --ink:#0d1520;
  --blue:#4697c8;
  --tile:#6aabd0;
  --title:#3a8fc2;
  --bg:#f6f4f5;
  --white:#ffffff;
  --text:#1b1f24;
}
*{margin:0;padding:0;box-sizing:border-box}
html,body{width:1200px;height:4530px;overflow:hidden}
body{background:var(--bg);font-family:'Lexend',sans-serif;color:var(--text);position:relative}
.abs{position:absolute}
.header{left:0;top:0;width:1200px;height:189px;background:var(--ink)}
.brand{display:flex;align-items:center;gap:18px;color:var(--white);font-weight:600;letter-spacing:1px}
.brand .mark{width:26px;height:26px;background:var(--blue)}
.header .brand{left:0;width:1200px;top:60px;justify-content:center;font-size:56px}
.lang{right:18px;top:160px;color:var(--white);font-size:13px}
.nav{left:0;top:189px;width:1200px;height:64px;background:var(--blue);display:flex;justify-content:center;align-items:center;gap:50px}
.nav a{color:var(--white);text-decoration:none;font-size:18px;font-weight:300;letter-spacing:.2px}
.photo{background:linear-gradient(135deg,#d9d9d9,#8a8a8a 55%,#3b3b3b)}
.arrow{width:44px;height:80px}
.hello{font-size:82px;font-weight:400;color:var(--title);line-height:1}
.sub{font-size:48px;font-weight:300;color:var(--title);line-height:1.3}
.body{font-size:23px;line-height:32px;font-weight:300;text-align:justify}
.more{color:var(--title)}
.tile{width:332px;height:280px;background:var(--tile);box-shadow:0 6px 10px rgba(0,0,0,.18);color:var(--white);text-align:center}
.tile svg{position:absolute;left:50%;top:38px;transform:translateX(-50%)}
.tile span{position:absolute;left:0;right:0;top:176px;font-size:31px;font-weight:400}
.card{background:var(--white);box-shadow:0 2px 8px rgba(0,0,0,.1);border-bottom:3px solid var(--tile)}
.svc{left:42px;width:500px}
.svc svg{position:absolute;left:0;top:10px}
.svc h3{margin-left:136px;font-size:30px;font-weight:300;color:var(--title)}
.svc p{margin-left:136px;font-size:18px;font-weight:300;line-height:24px}
.check{left:633px;display:flex;align-items:center;gap:32px;font-size:24px;font-weight:300}
.check i{width:44px;height:44px;background:var(--ink);border-radius:6px;display:flex;align-items:center;justify-content:center}
.ev h3{font-size:34px;font-weight:300;color:var(--title)}
.ev p{font-size:18px;font-weight:300;line-height:24.5px;text-align:justify}
.btn{background:var(--blue);color:var(--white);font-size:17px;font-weight:300;text-align:center;border-radius:3px}
.field{left:73px;width:587px;border:3px solid var(--blue);border-radius:5px;color:var(--title);font-size:31px;font-weight:300;padding:2px 14px;background:var(--bg)}
.footer{left:0;top:4392px;width:1200px;height:138px;background:var(--ink)}
.footer .brand{left:30px;top:45px;font-size:40px}
.footer ul{position:absolute;left:479px;top:34px;list-style:none;color:var(--white);font-size:22px;font-weight:300;line-height:31px}
</style>
</head>
<body>
<header class="abs header">
  <div class="abs brand"><span class="mark"></span>Weg zum Dialog</div>
  <div class="abs lang">DE ⌄</div>
</header>
<nav class="abs nav">
  <a>MEDIATION, COACHING, TEAMTRAINING</a><a>ÜBER UNS</a><a>PROJEKTE &amp; EVENTS</a><a>KONTAKT</a>
</nav>

<div class="abs photo" style="left:62px;top:290px;width:1068px;height:440px" role="img" aria-label="Schwarzweißfoto: Handschlag zweier Personen"></div>
<svg class="abs arrow" style="left:38px;top:470px" viewBox="0 0 44 80"><path d="M34 6 L10 40 L34 74" fill="none" stroke="var(--blue)" stroke-width="9"/></svg>
<svg class="abs arrow" style="left:1108px;top:470px" viewBox="0 0 44 80"><path d="M10 6 L34 40 L10 74" fill="none" stroke="var(--blue)" stroke-width="9"/></svg>

<h1 class="abs hello" style="left:62px;top:788px">Hallo.</h1>
<p class="abs sub" style="left:62px;top:868px;width:330px">Wir sind Berger &amp; Olsen.</p>
<p class="abs body" style="left:391px;top:790px;width:537px">Lorem ipsum dolor sit amet, consectetur adipiscing elit. Nunc vulputate libero et velit interdum, ac aliquet odio mattis. Class aptent taciti sociosqu ad litora torquent per conubia nostra, per inceptos himenaeos. <span class="more">Mehr Details →</span></p>
<div class="abs" style="left:974px;top:776px;font-size:24px;font-weight:300">Wilkommen!</div>
<div class="abs" style="left:1077px;top:816px;width:51px;height:3px;background:var(--blue)"></div>

<div class="abs tile" style="left:62px;top:1050px">
  <svg width="90" height="90" viewBox="0 0 90 90" fill="none" stroke="#fff" stroke-width="4"><path d="M22 80 V60 C10 50 12 18 40 12 C66 8 80 30 72 48 L74 58 H66 V80"/><path d="M44 30 L36 48 H48 L40 66"/></svg>
  <span>MEDIATION</span>
</div>
<div class="abs tile" style="left:431px;top:1050px">
  <svg width="90" height="90" viewBox="0 0 90 90" fill="none" stroke="#fff" stroke-width="3.5"><rect x="50" y="8" width="26" height="20"/><circle cx="22" cy="16" r="7"/><circle cx="45" cy="52" r="7"/><circle cx="18" cy="60" r="6"/><circle cx="72" cy="60" r="6"/><path d="M10 80 C10 70 26 70 26 80 M35 76 C35 64 55 64 55 76 M64 80 C64 70 80 70 80 80"/></svg>
  <span>COACHING</span>
</div>
<div class="abs tile" style="left:796px;top:1050px">
  <svg width="90" height="90" viewBox="0 0 90 90" fill="none" stroke="#fff" stroke-width="3.5"><path d="M15 8 V30 M45 8 V30 M75 8 V30 M30 8 V24 M60 8 V24"/><circle cx="45" cy="48" r="7"/><circle cx="28" cy="58" r="6"/><circle cx="62" cy="58" r="6"/><path d="M18 80 C18 68 38 68 38 80 M52 80 C52 68 72 68 72 80 M35 66 C35 56 55 56 55 66"/></svg>
  <span>TEAMTRAINING</span>
</div>

<div class="abs photo" style="left:35px;top:1413px;width:747px;height:407px;background:linear-gradient(90deg,#3a3634,#6b6764 30%,#dedede 45%,#e8e8e8 60%,#4a4644 80%,#2c2a29)" role="img" aria-label="Schwarzweißfoto: zwei Mediatoren im Anzug neben einem Flipchart vor einer Backsteinwand"></div>
<h2 class="abs hello" style="left:815px;top:1398px">Hallo.</h2>
<p class="abs sub" style="left:815px;top:1478px;font-size:46px">Das sind wir.</p>
<p class="abs body" style="left:820px;top:1580px;width:330px;font-size:18px;line-height:24.5px">Lorem ipsum dolor sit amet, consectetur adipiscing elit. Nunc vulputate libero et velit interdum, ac aliquet odio mattis. Class aptent taciti sociosqu ad litora torquent per conubia nostra, per inceptos himenaeos. Class aptent taciti sociosqu ad litora torquent per conubia nostra, per inceptos himenaeos.</p>

<div class="abs card" style="left:35px;top:1950px;width:554px;height:600px"></div>
<div class="abs svc" style="top:1978px">
  <svg width="80" height="60" viewBox="0 0 80 60" fill="none" stroke="var(--title)" stroke-width="3.5"><circle cx="14" cy="12" r="6"/><path d="M4 34 C4 24 24 24 24 34"/><rect x="4" y="36" width="32" height="14"/><rect x="40" y="14" width="32" height="14"/><circle cx="64" cy="44" r="6"/><path d="M46 58 C46 50 66 50 70 54"/></svg>
  <h3>Mediation</h3><p>Lorem ipsum dolor sit amet,<br>consectetur adipiscing elit.</p>
</div>
<div class="abs svc" style="top:2121px">
  <svg width="80" height="70" viewBox="0 0 80 70" fill="none" stroke="var(--title)" stroke-width="3.5"><path d="M20 6 H66 V34 H36 L26 42 V34 H20 Z"/><circle cx="16" cy="42" r="7"/><path d="M4 68 C4 52 28 52 30 60 L44 50"/><path d="M30 16 H56 M30 24 H50"/></svg>
  <h3>Vorträge</h3><p>Lorem ipsum dolor sit amet,<br>consectetur adipiscing elit.</p>
</div>
<div class="abs svc" style="top:2272px">
  <svg width="80" height="70" viewBox="0 0 80 70" fill="none" stroke="var(--title)" stroke-width="3.5"><rect x="30" y="4" width="16" height="34" rx="8"/><path d="M22 30 C22 50 54 50 54 30 M38 46 V62"/></svg>
  <h3>Training</h3><p>Lorem ipsum dolor sit amet,<br>consectetur adipiscing elit.</p>
</div>
<div class="abs svc" style="top:2422px">
  <svg width="80" height="70" viewBox="0 0 80 70" fill="none" stroke="var(--title)" stroke-width="3.5"><circle cx="38" cy="34" r="26"/><circle cx="38" cy="22" r="2" fill="var(--title)"/><path d="M34 30 H40 V48 M32 48 H46"/></svg>
  <h3>Beratung</h3><p>Lorem ipsum dolor sit amet,<br>consectetur adipiscing elit.</p>
</div>

<div class="abs check" style="top:1976px"><i><svg width="26" height="20" viewBox="0 0 26 20"><path d="M3 10 L10 17 L23 3" fill="none" stroke="#fff" stroke-width="4"/></svg></i>Verantwortungsbewusstsein</div>
<div class="abs check" style="top:2075px"><i><svg width="26" height="20" viewBox="0 0 26 20"><path d="M3 10 L10 17 L23 3" fill="none" stroke="#fff" stroke-width="4"/></svg></i>Seriösität</div>
<div class="abs check" style="top:2174px"><i><svg width="26" height="20" viewBox="0 0 26 20"><path d="M3 10 L10 17 L23 3" fill="none" stroke="#fff" stroke-width="4"/></svg></i>Engagement</div>
<div class="abs check" style="top:2273px"><i><svg width="26" height="20" viewBox="0 0 26 20"><path d="M3 10 L10 17 L23 3" fill="none" stroke="#fff" stroke-width="4"/></svg></i>Zielorientiert</div>
<div class="abs check" style="top:2371px"><i><svg width="26" height="20" viewBox="0 0 26 20"><path d="M3 10 L10 17 L23 3" fill="none" stroke="#fff" stroke-width="4"/></svg></i>Strategisch</div>
<div class="abs check" style="top:2470px"><i><svg width="26" height="20" viewBox="0 0 26 20"><path d="M3 10 L10 17 L23 3" fill="none" stroke="#fff" stroke-width="4"/></svg></i>Bildend</div>

<h2 class="abs hello" style="left:57px;top:2662px">Hallo.</h2>
<p class="abs sub" style="left:57px;top:2744px">Bock auf Events?</p>

<div class="abs card ev" style="left:73px;top:2849px;width:1068px;height:294px">
  <div class="abs photo" style="left:494px;top:0;width:574px;height:291px;background:linear-gradient(135deg,#2a2a2a,#7a7a7a 40%,#d8d8d8 55%,#3a3a3a)" role="img" aria-label="Schwarzweißfoto: Vortrag vor einer großen Projektionsleinwand"></div>
  <h3 class="abs" style="left:22px;top:20px">Business Coaching</h3>
  <p class="abs" style="left:22px;top:72px;width:430px">Lorem ipsum dolor sit amet, consectetur adipiscing elit. Nunc vulputate libero et velit interdum, ac aliquet odio mattis. Class aptent taciti sociosqu ad litora torquent per conubia nostra, per inceptos himenaeos.</p>
  <div class="abs btn" style="left:22px;top:237px;width:151px;height:31px;line-height:31px">Buchen</div>
</div>

<div class="abs card ev" style="left:70px;top:3187px;width:1071px;height:295px">
  <div class="abs photo" style="left:0;top:0;width:572px;height:292px;background:linear-gradient(90deg,#2e2e2e,#8a8a8a 35%,#c8c8c8 60%,#5a5a5a)" role="img" aria-label="Schwarzweißfoto: zwei Frauen im Gespräch vor einer Fensterfront"></div>
  <h3 class="abs" style="right:46px;top:18px">Private Coaching</h3>
  <p class="abs" style="left:616px;top:80px;width:431px">Lorem ipsum dolor sit amet, consectetur adipiscing elit. Nunc vulputate libero et velit interdum, ac aliquet odio mattis. Class aptent taciti sociosqu ad litora torquent per conubia nostra, per inceptos himenaeos.</p>
  <div class="abs btn" style="left:888px;top:237px;width:154px;height:31px;line-height:31px">Buchen</div>
</div>

<div class="abs field" style="top:3620px;height:44px">Name</div>
<div class="abs field" style="top:3701px;height:44px">E-Mail Adresse</div>
<div class="abs field" style="top:3781px;height:369px">Ihre Nachricht</div>
<div class="abs" style="left:73px;top:4190px;width:44px;height:44px;background:var(--blue);border-radius:5px"><svg width="44" height="44" viewBox="0 0 44 44"><path d="M12 22 L19 29 L32 15" fill="none" stroke="#fff" stroke-width="4"/></svg></div>
<div class="abs" style="left:147px;top:4193px;font-size:28px;font-weight:300">Abboniere den Newsletter.</div>
<div class="abs btn" style="left:73px;top:4268px;width:587px;height:53px;line-height:53px;font-size:30px">Absenden</div>

<h2 class="abs hello" style="right:72px;top:3596px">Hallo.</h2>
<p class="abs sub" style="right:72px;top:3676px">Get Connected.</p>
<div class="abs photo" style="left:743px;top:3778px;width:387px;height:548px;background:linear-gradient(160deg,#f2f2f2,#d4d4d4 45%,#3a3a3a 60%,#111)" role="img" aria-label="Schwarzweißfoto: Tastatur und Tablet mit Stift auf einem Schreibtisch"></div>

<footer class="abs footer">
  <div class="abs brand"><span class="mark" style="width:20px;height:20px"></span>Weg zum Dialog</div>
  <ul><li>Impressum</li><li>Datenschutz</li><li>Kontakt</li></ul>
</footer>
</body>
</html>
```